Business Card Design Project

I need a cool business card design for the company that will build residential houses.
The card should include:
1) Name: Boris Kalinov
2) Cell: 587.204.XXXX
3) Email: bor.kalinov@qwvend.example
4) Position: General Manager
5) Residential Home Building
6) Company logo that I have uploaded

Industry/Entity Type

Residential

```html
<!DOCTYPE html>
<html lang="en">
<head>
<meta charset="utf-8">
<title>QWVEND Business Card</title>
<link rel="stylesheet" href="https://fonts.googleapis.com/css2?family=Parisienne&display=swap">
<style>
  :root {
    --page-bg: #ece9e4;
    --card-bg: #ffffff;
    --ink: #2a2a2a;
    --brand-blue: #1f4f9a;
    --brand-green: #3aa24a;
    --rule: #b9b9b9;
    --roof: #e9b6a4;
    --wall: #dde6f2;
  }
  * { margin: 0; padding: 0; box-sizing: border-box; }
  html, body {
    width: 1200px;
    height: 1200px;
    overflow: hidden;
    background: var(--page-bg);
  }
  .canvas {
    width: 1200px;
    height: 1200px;
    display: flex;
    flex-direction: column;
    align-items: center;
    justify-content: center;
    gap: 60px;
  }
  .card {
    position: relative;
    width: 840px;
    height: 480px;
    background: var(--card-bg);
    box-shadow: 0 4px 16px rgba(0,0,0,0.12);
    overflow: hidden;
  }
  .brand {
    position: absolute;
    left: 40px;
    top: 60px;
    display: flex;
    align-items: center;
    gap: 10px;
    font-family: "Parisienne", cursive;
    font-size: 40px;
    line-height: 1;
    color: var(--brand-blue);
  }
  .brand-dot {
    width: 20px;
    height: 20px;
    border-radius: 50%;
    background: var(--brand-green);
  }
  .tagline {
    position: absolute;
    left: 72px;
    top: 112px;
    font-family: "Parisienne", cursive;
    font-size: 20px;
    line-height: 1;
    color: var(--brand-blue);
  }
  .house-art {
    position: absolute;
    left: 580px;
    top: 30px;
    width: 220px;
    height: 220px;
    border-radius: 10px;
    background: linear-gradient(180deg, var(--roof) 0%, var(--roof) 38%, var(--wall) 38%, #f3f6fb 100%);
    opacity: 0.8;
  }
  .details {
    font-family: "Parisienne", cursive;
    color: var(--ink);
    font-size: 30px;
    line-height: 1;
  }
  .details p { position: absolute; white-space: nowrap; }
  .details .name  { left: 140px; top: 160px; }
  .details .title { left: 140px; top: 214px; }
  .details .phone { left: 150px; top: 268px; }
  .details .email { left: 170px; top: 370px; }
  .rule {
    position: absolute;
    height: 1px;
    background: var(--rule);
  }
  .rule-mid { left: 430px; right: 30px; top: 330px; }
  .rule-base { left: 80px; right: 30px; top: 440px; }
</style>
</head>
<body>
  <main class="canvas">
    <section class="card card-front">
      <div class="brand">
        <span class="brand-dot"></span>
        <span class="brand-name">QWVEND</span>
      </div>
      <p class="tagline">Residential Home Building</p>
      <div class="house-art" role="img" aria-label="Soft illustration of a small house with a pink roof"></div>
      <div class="details">
        <p class="name">Boris Kalinov</p>
        <p class="title">General Manager</p>
        <p class="phone">587.204.XXXX</p>
        <p class="email">bor.kalinov@qwvend.example</p>
      </div>
      <div class="rule rule-mid"></div>
      <div class="rule rule-base"></div>
    </section>
    <section class="card card-back" aria-label="Card back"></section>
  </main>
</body>
</html>
```